Business Card for staff member of football club SC Brenval

I would like to get a business card template for all staff member of our soccer club.

The card should use as much as possible the 2 colors of the club : Red which is the main color and blue which is the alternative color. It can be balanced between the two like our logo.

I prefer simple and lean design.

Contact Information for Business Card

Bussiness card should have all main stuff as describe here below in must have.

Font styles to use
Sans Serif

Requirements
Must have
• Name : Laurent DESPRATIN
Fonction : Président
Mobile : +41 xx xxx xx xx
Email : first.lastname@scbrenval.ch
Adresse of the club : SC Brenval, 1873 Brenval
Website of the club : www.scbrenval.ch
Nice to have
• Version with and without picture of the staff member

A version for men, a version for women staff member.

```html
<!DOCTYPE html>
<html lang="fr">
<head>
<meta charset="utf-8">
<title>SC Brenval – Carte de visite</title>
<link rel="stylesheet" href="https://fonts.googleapis.com/css2?family=Oswald:wght@500;700&family=Arimo:wght@400&display=swap">
<style>
  :root {
    --backdrop: #2b2b2b;
    --card: #0c0c0c;
    --club-red: #e8203a;
    --club-blue: #0a86cf;
    --white: #f2f2f2;
    --grey: #bdbdbd;
    --rule: #2e2e2e;
  }
  * { box-sizing: border-box; margin: 0; padding: 0; }
  html, body { width: 1200px; height: 900px; overflow: hidden; }
  body {
    background: radial-gradient(ellipse at 50% 40%, #3a3a3a 0%, var(--backdrop) 60%, #1c1c1c 100%);
    position: relative;
    font-family: "Arimo", Arial, sans-serif;
  }
  .card {
    position: absolute;
    width: 600px;
    height: 343px;
    background: var(--card);
    box-shadow: 0 18px 40px rgba(0,0,0,.6);
  }
  .card--front { left: 70px; top: 70px; }
  .card--back { left: 530px; top: 487px; }

  .club-mark {
    display: flex;
    flex-direction: column;
    align-items: center;
    gap: 16px;
  }
  .club-mark__dot {
    width: 64px; height: 64px;
    border-radius: 50%;
    background: var(--club-red);
  }
  .club-mark__name {
    font-family: "Oswald", "Arial Narrow", sans-serif;
    font-weight: 700;
    font-size: 30px;
    letter-spacing: .5px;
    color: var(--white);
    text-transform: uppercase;
  }

  .card--front .club-mark {
    position: absolute;
    left: 20px; top: 0; width: 200px; height: 100%;
    justify-content: center;
  }
  .divider {
    position: absolute;
    left: 232px; top: 50px;
    width: 1px; height: 243px;
    background: var(--rule);
  }
  .details {
    position: absolute;
    left: 262px; top: 78px;
  }
  .person__name {
    font-family: "Oswald", "Arial Narrow", sans-serif;
    font-weight: 500;
    font-size: 30px;
    line-height: 1;
    text-transform: uppercase;
    letter-spacing: -.3px;
  }
  .person__first { color: var(--club-red); }
  .person__last { color: var(--club-blue); }
  .person__role {
    color: var(--grey);
    font-size: 16px;
    margin-top: 6px;
  }
  .contact { list-style: none; margin-top: 18px; }
  .contact li {
    display: flex; align-items: center; gap: 10px;
    color: var(--grey);
    font-size: 15px;
    line-height: 24px;
  }
  .contact li.contact__address { margin-top: 12px; }
  .contact svg { width: 15px; height: 15px; flex: none; fill: var(--club-red); }

  .card--back .club-mark {
    position: absolute; inset: 0;
    justify-content: center;
  }
  .card--back .club-mark__dot { width: 84px; height: 84px; }
  .card--back .club-mark__name { font-size: 38px; }
</style>
</head>
<body>
  <section class="card card--front">
    <div class="club-mark">
      <span class="club-mark__dot"></span>
      <span class="club-mark__name">SC Brenval</span>
    </div>
    <span class="divider"></span>
    <div class="details">
      <h1 class="person__name"><span class="person__first">Laurent</span> <span class="person__last">Despratin</span></h1>
      <p class="person__role">Président</p>
      <ul class="contact">
        <li>
          <svg viewBox="0 0 16 16" aria-hidden="true"><path d="M3.6 1.2l2.3 2.6-1.3 1.8c.9 2 2.6 3.7 4.6 4.6l1.8-1.3 2.6 2.3-1.4 2.4C6.8 14.8 1.2 9.2 1.2 3.8z"/></svg>
          +41 xx xxx xx xx
        </li>
        <li>
          <svg viewBox="0 0 16 16" aria-hidden="true"><path d="M1 3h14v10H1z M2.5 4.5v.3L8 9l5.5-4.2v-.3z" fill-rule="evenodd"/></svg>
          first.lastname@scbrenval.ch
        </li>
        <li>
          <svg viewBox="0 0 16 16" aria-hidden="true"><path d="M8 1a7 7 0 100 14A7 7 0 008 1zm0 1.5c.8 0 1.7 1.6 2 4h-4c.3-2.4 1.2-4 2-4zm-2.1 5.5h4.2c-.2 2.7-1.2 5.5-2.1 5.5s-1.9-2.8-2.1-5.5zM2.6 8h2c.1 1.8.5 3.4 1 4.5A5.5 5.5 0 012.6 8zm8.8 0h2a5.5 5.5 0 01-3 4.5c.5-1.1.9-2.7 1-4.5zM2.6 6.5a5.5 5.5 0 013-4c-.5 1.1-.9 2.5-1 4zm8.8 0c-.1-1.5-.5-2.9-1-4a5.5 5.5 0 013 4z"/></svg>
          www.scbrenval.ch
        </li>
        <li class="contact__address">
          <svg viewBox="0 0 16 16" aria-hidden="true"><path d="M8 1a5 5 0 00-5 5c0 3.6 5 9 5 9s5-5.4 5-9a5 5 0 00-5-5zm0 7a2 2 0 110-4 2 2 0 010 4z"/></svg>
          SC Brenval, 1873 Brenval
        </li>
      </ul>
    </div>
  </section>

  <section class="card card--back">
    <div class="club-mark">
      <span class="club-mark__dot"></span>
      <span class="club-mark__name">SC Brenval</span>
    </div>
  </section>
</body>
</html>
```